The Christian Teacher Life-Cycle

Look at the Lifecyle of the Christian School.
Look at the BLT logo.
I am looking for a Christian Teacher Lifecycle that represents the slides in the PP upload.
Our website is bramblewoodlearningtrust.org.
The design should include a summary design showing all four stages, and then four slides representing each of the stages as subsets of the summary design.
When a teacher is going through the Lifecycle, they are going on their Professional Learning Journey that takes 40 years to unfold.
All five should include a copyright 2026 BLT on them.

```html
<!DOCTYPE html>
<html lang="en">
<head>
<meta charset="UTF-8">
<title>Learning Journey – Step 2</title>
<link rel="stylesheet" href="https://fonts.googleapis.com/css2?family=Poppins:wght@400;600&family=Tinos:wght@700&display=swap">
<style>
  :root {
    --ink-navy: #0c335d;
    --brand-blue: #1b7bbf;
    --step-teal: #0d6a5e;
    --text-dark: #121212;
    --text-muted: #6b6b6b;
    --paper: #ffffff;
    --sky-gold: #e6d48a;
    --hill-light: #8fae4a;
    --hill-mid: #557a2a;
    --hill-deep: #2f4e1c;
  }
  * { margin: 0; padding: 0; box-sizing: border-box; }
  html, body { width: 1200px; height: 675px; overflow: hidden; background: var(--paper); }
  .slide {
    position: relative;
    width: 1200px;
    height: 675px;
    background: var(--paper);
    overflow: hidden;
  }
  .brand {
    position: absolute;
    left: 56px;
    top: 42px;
    font-family: "Poppins", sans-serif;
    font-weight: 600;
    font-size: 28px;
    line-height: 1;
    letter-spacing: 1px;
    color: var(--brand-blue);
  }
  .slide-title {
    position: absolute;
    left: 49px;
    top: 102px;
    font-family: "Tinos", "Times New Roman", serif;
    font-weight: 700;
    font-size: 57px;
    line-height: 1;
    color: var(--ink-navy);
  }
  .step-badge {
    position: absolute;
    left: 47px;
    top: 189px;
    width: 220px;
    height: 54px;
    border-radius: 27px;
    background: var(--step-teal);
    color: var(--paper);
    font-family: "Tinos", "Times New Roman", serif;
    font-weight: 700;
    font-size: 46px;
    line-height: 54px;
    padding-left: 37px;
    padding-top: 2px;
  }
  .journey-points {
    position: absolute;
    left: 51px;
    top: 265px;
    width: 678px;
    list-style: none;
    font-family: "Poppins", sans-serif;
    font-weight: 600;
    font-size: 25.4px;
    line-height: 39px;
    color: var(--text-dark);
  }
  .journey-points li {
    position: relative;
    padding-left: 16px;
    margin-bottom: 14px;
  }
  .journey-points li::before {
    content: "•";
    position: absolute;
    left: 0;
    top: 0;
  }
  .copyright {
    position: absolute;
    left: 56px;
    bottom: 16px;
    font-family: "Poppins", sans-serif;
    font-weight: 400;
    font-size: 11px;
    line-height: 1;
    color: var(--text-muted);
  }
  .scene-panel {
    position: absolute;
    left: 767px;
    top: 0;
    width: 433px;
    height: 675px;
    background: linear-gradient(180deg, var(--sky-gold) 0%, #cbc98a 22%, var(--hill-light) 42%, var(--hill-mid) 68%, var(--hill-deep) 100%);
  }
</style>
</head>
<body>
  <main class="slide">
    <div class="brand">BLT</div>
    <h1 class="slide-title">Learning Journey</h1>
    <div class="step-badge">STEP 2</div>
    <ul class="journey-points">
      <li>My Christian Professional Learning Community is important to me as a place where I give and take</li>
      <li>I recognize that “we” is more powerful for the child than “I”</li>
      <li>I know my curriculum - I am more focused on how, on pedagogy</li>
      <li>I assess relevant and effective assessment tools</li>
      <li>I reflect on my practice</li>
    </ul>
    <p class="copyright">© 2026 BLT</p>
    <div class="scene-panel" role="img" aria-label="Painted landscape: four teachers walking up a winding path through green hills toward a church on a hilltop, mountains and a golden sky behind"></div>
  </main>
</body>
</html>
```